Business card and stationery design

Harbourlight Gatherings Co. is a leading event and conference design and management company.
Please view lumorahostgroup.com.au

The business cards needs to convey:
- professionalism and competency
- exclusivity
- memorable experiences and quality

The business card needs to have the following aspects:
- double sided
- Full colour CMYK
- Printed on either high gloss matt card (designer to recommend)

For the business stationery we require:
- Letterhead with top banner and bottom footer
- A thank you card design
- a with compliments slip design
- a MS powerpoint and MS publisher client presentation slide design which includes cover page and then a standard presentation page
(Note- we do NOT require an envelope design- who sends letters these days!)

The company image is using the key colours of gold, silver and black.
A black background to the business card has been used before and is preferred although we are open to options.

Target Market(s)

High end corporations and businesses that require their events and conferences to be exceptionally well designed and managed

Industry/Entity Type

Business

Contact Information for Business Card

FRONT:

Darian Whitlock
- Event and Conference Specialist

Mobile- +61 (0) 491 238 604
Office- 1300 617 482
dariannw@lumorahostgroup.com.au

Web- lumorahostgroup.com.au

BACK:

- Event and

Font styles to use
Other font styles liked:
• The logo designer used Trajan Pro Bold 3 for the font text in the logo

Requirements
Must have
• Amazing design of the following:
• - business card (double sided)
• - letterhead
• - client thank you card
• - powerpoint and publisher client presentation design files

```html
<!DOCTYPE html>
<html lang="en">
<head>
<meta charset="utf-8">
<title>Harbourlight Gatherings Co. — Business Card</title>
<link rel="stylesheet" href="https://fonts.googleapis.com/css2?family=Cinzel:wght@700&family=Didact+Gothic&display=swap">
<style>
  :root {
    --bg: #1c1c1d;
    --card: #0b0b0c;
    --card-edge: #18181a;
    --gold: #cf9c2e;
    --gold-light: #e2b54c;
    --silver: #c9c9cc;
    --ink: #141414;
    --web-gold: #c99a3a;
  }
  * { margin: 0; padding: 0; box-sizing: border-box; }
  html, body { width: 1200px; height: 969px; overflow: hidden; background: var(--bg); }
  body { position: relative; font-family: "Didact Gothic", "Century Gothic", sans-serif; }

  .card {
    position: absolute;
    width: 580px;
    height: 340px;
    border-radius: 22px;
    background: linear-gradient(135deg, var(--card-edge) 0%, var(--card) 55%, #050505 100%);
    overflow: hidden;
    box-shadow: 0 18px 40px rgba(0,0,0,0.55);
  }

  /* Back side */
  .card-back { left: 560px; top: 80px; }
  .brand {
    position: absolute;
    left: 0; right: 0; top: 78px;
    text-align: center;
  }
  .brand-mark {
    display: block;
    width: 86px; height: 86px;
    margin: 0 auto 22px;
    border-radius: 50%;
    background: radial-gradient(circle at 40% 35%, var(--gold-light), var(--gold) 70%);
  }
  .brand-name {
    font-family: "Cinzel", "Trajan Pro", serif;
    font-weight: 700;
    font-size: 27px;
    letter-spacing: 1px;
    color: var(--silver);
  }
  .brand-rule {
    width: 340px; height: 1px;
    margin: 12px auto 0;
    background: var(--gold);
  }
  .brand-web {
    margin-top: 18px;
    font-size: 17px;
    letter-spacing: 0.5px;
    color: var(--silver);
  }
  .brand-web span { color: var(--web-gold); }

  /* Front side */
  .card-front { left: 80px; top: 520px; }
  .front-mark {
    position: absolute;
    left: 300px; top: 28px;
    width: 96px; height: 96px;
    border-radius: 50%;
    background: radial-gradient(circle at 40% 35%, var(--gold-light), var(--gold) 70%);
  }
  .band {
    position: absolute;
    left: 0; right: 0; top: 156px;
    height: 122px;
    background: linear-gradient(90deg, var(--gold) 0%, var(--gold-light) 45%, var(--gold) 100%);
    display: flex;
    align-items: center;
    color: var(--ink);
  }
  .person { width: 240px; padding-left: 26px; }
  .person-name {
    font-weight: 700;
    font-size: 19px;
    letter-spacing: 0.5px;
    text-transform: uppercase;
    -webkit-text-stroke: 0.4px var(--ink);
  }
  .person-title { font-size: 15px; margin-top: 4px; }
  .divider { width: 1px; height: 84px; background: rgba(20,20,20,0.55); margin-right: 18px; }
  .contacts { list-style: none; font-size: 14.5px; line-height: 1.55; }
  .contacts li { display: flex; align-items: center; gap: 9px; }
  .contacts svg { width: 14px; height: 14px; flex: none; }
  .contacts .web { font-size: 16px; font-weight: 700; -webkit-text-stroke: 0.3px var(--ink); }
</style>
</head>
<body>

<section class="card card-back" aria-label="Business card back">
  <div class="brand">
    <span class="brand-mark"></span>
    <div class="brand-name">Harbourlight Gatherings Co.</div>
    <div class="brand-rule"></div>
    <div class="brand-web">www.<span>lumorahostgroup.com.au</span></div>
  </div>
</section>

<section class="card card-front" aria-label="Business card front">
  <span class="front-mark"></span>
  <div class="band">
    <div class="person">
      <div class="person-name">Darian Whitlock</div>
      <div class="person-title">Event and Conference Specialist</div>
    </div>
    <div class="divider"></div>
    <ul class="contacts">
      <li>
        <svg viewBox="0 0 14 14"><rect x="3.5" y="1" width="7" height="12" rx="1.5" fill="none" stroke="#141414" stroke-width="1.3"/><circle cx="7" cy="11" r="0.8" fill="#141414"/></svg>
        +61 (0) 491 238 604
      </li>
      <li>
        <svg viewBox="0 0 14 14"><path d="M1 5 Q7 1 13 5 L11 6.5 L9.5 5 L4.5 5 L3 6.5 Z" fill="#141414"/><rect x="3" y="7" width="8" height="5" rx="1" fill="#141414"/></svg>
        1300 617 482
      </li>
      <li>
        <svg viewBox="0 0 14 14"><rect x="1" y="3" width="12" height="8" fill="#141414"/><path d="M1 3 L7 8 L13 3" fill="none" stroke="#e2b54c" stroke-width="1"/></svg>
        dariannw@lumorahostgroup.com.au
      </li>
      <li class="web">
        <svg viewBox="0 0 14 14"><circle cx="7" cy="7" r="5.8" fill="none" stroke="#141414" stroke-width="1.2"/><ellipse cx="7" cy="7" rx="2.5" ry="5.8" fill="none" stroke="#141414" stroke-width="1"/><line x1="1.2" y1="7" x2="12.8" y2="7" stroke="#141414" stroke-width="1"/></svg>
        www.lumorahostgroup.com.au
      </li>
    </ul>
  </div>
</section>

</body>
</html>
```